Vesta Power Web Design

I want a design for a home page that can function as a template for the entire web design. I"m also requesting that the design be adapted as a template for Power Point presentations, as well.

Here"s a brief about our company:

Vesta Power provides its customers with clean, redundant and reliable power. Functioning as a private power producer, Vesta Power owns and operates combined heat and power (CHP) and distributed generation (DG) systems.

Vesta’s management has extensive experience in aerospace turbines engine operation, maintenance, manufacturing and repair. Depending on the customer need, Vesta either builds new generators or refurbish “retired” aerospace turbines into industrial generators. This allows Vesta to deliver generating systems at greatly reduced capital outlays, enabling Vesta Power to offer its customers not only redundant power and grid independence, but significant savings on their energy needs. Vesta’s typical installation size is 500Kws to 3Mws but based upon our customer"s needs, Vesta can site multiple generators to configure systems of larger size.

By using aero derivative turbine engines the company has the flexibility to use the best source of fuel for each site and power requirement. The turbine engine can operate on virtually any combustible fuel. This allows Vesta to utilize the flex fuel practice and operate on either the least expensive fuel available or operate on renewable and biofuels to fulfill the green power requirements mandated by many federal, state and local utility commissions.

Vesta’s market strategy is as follows:

1. Sell reliable and redundant power through a PPAs or lease agreements to industrial or institutional customers with high electrical and thermal needs such as food processors, bio fuel producers, hospitals, casinos, hotels, etc.

2. Lease its systems to customer that “flare gas” as byproducts of their processes such as wastewater treatment facilities, land fills and "stranded gas wells" allowing them to use their waste products to power their facilities and sell excess electricity back to the grid.

3. Partner with other private power producers to provide the turbine generating capacity on a leased basis.
Updates

Please disregard the "turbine logo" that was uploaded as a file and focus only on the "bolt design logo", A (bolt) E.

We like the simple navigation and clean and modern design of sites.

http://www.plumvault.example/

http://www.serviqo.example/

http://www.trylumo.example/

Target Market(s)

Our target markets can be found on the web architecture file I've attached to this submission.

Number of Pages Required

1 page

Requirements
Must have
• The designer must provide a web design and a Power Point template based upon the web design.

• The design must contemplate the web architecture that I""ve included as a file.

```html
<!DOCTYPE html>
<html lang="en">
<head>
<meta charset="utf-8">
<title>Vesta Power – Web and Slide Templates</title>
<link href="https://fonts.googleapis.com/css2?family=Questrial&display=swap" rel="stylesheet">
<style>
:root{
  --forest:#0b4a24;
  --forest-deep:#063a1c;
  --lime:#b3d700;
  --lime-soft:#d6ec6a;
  --cream:#f5fbdc;
  --cream-pale:#fbfdf0;
  --sky-top:#7ec3ea;
  --sky-low:#cfe9f6;
  --grass:#5ea528;
  --grass-dark:#3d7f18;
  --leaf-light:#b9dc5a;
  --leaf-mid:#8cc33a;
  --leaf-dark:#5b9420;
  --ink:#0e4a22;
  --white:#ffffff;
}
*{box-sizing:border-box;margin:0;padding:0}
html,body{width:1200px;height:2531px;overflow:hidden}
body{position:relative;font-family:"Questrial",sans-serif;color:var(--ink);background:var(--forest-deep)}
.page{position:absolute;left:0;width:1200px;overflow:hidden;
  background:linear-gradient(180deg,var(--sky-top) 0%,var(--sky-low) 80%,var(--grass) 92%,var(--grass-dark) 100%)}
.page--home{top:0;height:797px}
.page--inner{top:797px;height:850px}
.card{position:absolute;left:41px;width:1116px;background:var(--white);border-radius:0 0 12px 12px;box-shadow:0 3px 6px rgba(0,0,0,.3)}
.page--home .card{top:0;height:759px}
.page--inner .card{top:0;height:762px}
.topband{position:absolute;left:12px;right:8px;top:0;height:447px;background:linear-gradient(180deg,var(--lime) 0,var(--cream) 22px,var(--cream) 100%);border-radius:0 0 14px 14px}
.utility{position:absolute;right:26px;top:0;width:172px;height:18px;background:var(--cream);display:flex;justify-content:space-around;align-items:center}
.utility svg{width:14px;height:12px}
.brand{position:absolute;left:35px;top:36px;width:156px;height:148px;background:var(--forest);display:flex;align-items:center;justify-content:center;color:var(--lime);font-size:24px;text-align:center;line-height:1.1}
.nav{position:absolute;left:14px;top:205px;width:200px;list-style:none}
.nav li{height:35px;border-bottom:2px solid var(--lime);font-size:17px;padding:7px 0 0 12px;position:relative;white-space:nowrap}
.nav li.current::before{content:"";position:absolute;left:0;top:12px;border-left:11px solid var(--ink);border-top:6px solid transparent;border-bottom:6px solid transparent}
.main{position:absolute;left:218px;top:18px;width:872px;height:410px;background:var(--white);border:3px solid var(--lime);border-top:none;border-radius:0 0 10px 10px}
.intro{position:absolute;left:20px;top:68px;width:250px;font-size:14.8px;line-height:16.4px}
.player{position:absolute;left:280px;top:20px;width:554px;height:369px;box-shadow:2px 3px 6px rgba(0,0,0,.35)}
.player__bar{height:12px;background:linear-gradient(#ddd,#aaa);display:flex;gap:4px;padding:2px 4px}
.player__bar i{width:7px;height:7px;border-radius:50%;background:#d44}
.player__bar i+i{background:#e9b53a}.player__bar i+i+i{background:#6b3}
.player__scene{height:314px;background:linear-gradient(180deg,#5aaee6 0%,#b6dcf2 68%,#6aaa2c 76%,#3f8319 100%);position:relative}
.player__brand{position:absolute;left:192px;top:38px;width:157px;height:148px;background:var(--forest);display:flex;align-items:center;justify-content:center;color:var(--lime);font-size:23px}
.player__title{position:absolute;left:0;right:0;top:198px;text-align:center;font-size:32px;color:var(--forest)}
.player__controls{height:43px;background:linear-gradient(#e8e8e8,#9a9a9a);position:relative}
.player__controls .search{position:absolute;left:10px;top:15px;width:128px;height:13px;border-radius:7px;background:#fff}
.player__controls .btns{position:absolute;left:154px;top:10px;display:flex;gap:4px}
.player__controls .btns span{width:20px;height:20px;border-radius:50%;background:linear-gradient(#fff,#bbb);border:1px solid #888}
.player__controls .time{position:absolute;left:290px;top:12px;width:162px;height:18px;background:#222;border-radius:3px;color:#ccc;font-size:8px;padding:4px 8px;display:flex;justify-content:space-between}
.player__controls .vol{position:absolute;left:476px;top:20px;width:64px;height:3px;background:#444}
.article{position:absolute;left:14px;top:18px;right:40px;font-size:15.2px;line-height:16.4px;height:370px;overflow:hidden}
.article h1{font-weight:400;font-size:23px;margin-bottom:14px}
.article p{margin-bottom:16px}
.scroll{position:absolute;right:8px;top:14px;width:14px;height:376px;background:var(--lime-soft);border:2px solid var(--lime)}
.scroll::before,.scroll::after{content:"";position:absolute;left:0;border-left:6px solid transparent;border-right:6px solid transparent}
.scroll::before{top:2px;border-bottom:10px solid var(--forest)}
.scroll::after{bottom:2px;border-top:10px solid var(--forest)}
.tile{position:absolute;top:459px;height:241px;border:3px solid var(--lime);background:linear-gradient(180deg,var(--cream-pale),var(--lime-soft))}
.page--inner .tile{top:462px}
.tile--services{left:12px;width:200px}
.tile--contact{left:900px;width:205px}
.tile__label{position:absolute;left:14px;top:14px;height:20px;padding:2px 10px 0 30px;background:var(--lime);border-radius:10px;color:var(--white);font-size:14.5px;white-space:nowrap}
.tile__label::before{content:"";position:absolute;left:0;top:-6px;width:28px;height:28px;border-radius:50% 0;background:var(--grass)}
.tile p{position:absolute;left:10px;right:8px;top:54px;font-size:12.3px;line-height:16.4px}
.feature{position:absolute;left:222px;top:459px;width:668px;height:241px;border:3px solid var(--lime);border-radius:10px;overflow:hidden;background:var(--forest);display:flex}
.page--inner .feature{top:462px}
.feature__photo{width:224px;flex:none;height:100%;background:linear-gradient(160deg,var(--leaf-light),var(--leaf-mid) 55%,var(--leaf-dark))}
.feature__text{flex:1;color:var(--white);font-size:14.6px;line-height:17.6px;padding:4px 6px 0 11px}
.feature__text p+p{margin-top:17px}
.footer{position:absolute;left:0;right:0;top:714px;text-align:center;font-size:14.6px;line-height:18px}
.page--inner .footer{top:717px}
.page--slide{top:1647px;height:884px;background:var(--forest-deep)}
.slide__frame{position:absolute;left:19px;top:13px;width:1162px;height:871px;background:linear-gradient(180deg,#9fd4ef 0%,#d9effa 60%,#bfe3f4 80%,#6aa82e 88%,#3d7f18 100%)}
.slide__panel{position:absolute;left:119px;top:124px;width:924px;height:716px;background:linear-gradient(180deg,#e2edc6 0%,var(--cream-pale) 60%,#f5f9ea 100%)}
.slide__rule{position:absolute;left:108px;top:112px;width:949px;height:12px;background:var(--lime)}
.slide__brand{position:absolute;left:137px;top:8px;width:151px;height:144px;background:var(--forest);display:flex;align-items:center;justify-content:center;color:var(--lime);font-size:23px}
</style>
</head>
<body>

<section class="page page--home">
  <div class="card">
    <div class="topband">
      <div class="utility">
        <svg viewBox="0 0 14 12"><path d="M1 6 7 1l6 5M3 5v6h8V5" fill="none" stroke="#b3d700" stroke-width="1.5"/></svg>
        <svg viewBox="0 0 14 12"><rect x="1" y="2" width="12" height="8" fill="none" stroke="#b3d700" stroke-width="1.5"/><path d="M1 2l6 5 6-5" fill="none" stroke="#b3d700" stroke-width="1.5"/></svg>
        <svg viewBox="0 0 14 12"><path d="M7 1v4M2 5h10M2 5v3M7 5v3M12 5v3" fill="none" stroke="#b3d700" stroke-width="1.5"/></svg>
      </div>
      <div class="brand">Vesta Power</div>
      <ul class="nav">
        <li class="current">About Vesta</li><li>CHP</li><li>Stranded Gas</li><li>Resources</li><li>Partners And Suppliers</li><li>Contact Us</li>
      </ul>
      <div class="main">
        <p class="intro">Lorem ipsum dolor sit amet, consectetur adipiscing elit. Pellentesque tempus, magna vel fermentum consequat, orci odio lobortis eros, ut iaculis turpis ipsum ac dolor. Praesent mollis fermentum nunc ut condimentum. Maecenas vehicula eros metus, eu venenatis enim. Pellentesque eget est et justo semper dapibus. Suspendisse ut pharetra lectus. Suspendisse ut volutpat lectus. Cras turpis magna, iaculis id suscipit ut, aliquam at quam. Nam mattis mi ac odio pretium porta. In blandit lorem a lectus molestie scelerisque auctor massa consequat.</p>
        <div class="player">
          <div class="player__bar"><i></i><i></i><i></i></div>
          <div class="player__scene" role="img" aria-label="Video still: sky over green hill with company name">
            <div class="player__brand">Vesta Power</div>
            <div class="player__title">About Vesta</div>
          </div>
          <div class="player__controls">
            <span class="search"></span>
            <div class="btns"><span></span><span></span><span></span><span></span><span></span></div>
            <div class="time"><span>5:30</span><span>-5:54</span></div>
            <span class="vol"></span>
          </div>
        </div>
      </div>
    </div>
    <div class="tile tile--services"><span class="tile__label">Our Services</span><p>Lorem ipsum dolor sit amet, consectetur adipiscing elit. Pellentesque tempus, magna vel fermentum consequat, orci odio lobortis eros, ut iaculis turpis ipsum ac dolor. Praesent mollis fermentum nunc ut condimentum. Maecenas vehicula eros metus, eu venenatis enim.</p></div>
    <div class="feature">
      <div class="feature__photo" role="img" aria-label="Photo: water droplet on a green leaf"></div>
      <div class="feature__text"><p>Vesta Power provides its customers with clean, redundant and reliable power. Functioning as a private power producer, Vesta Power owns and operates combined heat and power (CHP) and distributed generation (DG) systems.</p><p>By using aero derivative turbine engines the company has the flexibility to use the best source of fuel for each site and power requirement. The turbine engine can operate on virtually any combustible fuel. This allows Vesta to utilize the flex fuel practice and operate on either the least expensive fuel available or operate on renewable and biofuels to fulfill the green power requirements mandated by many federal, state and local utility commissions.</p></div>
    </div>
    <div class="tile tile--contact"><span class="tile__label">Contac Us</span><p>Lorem ipsum dolor sit amet, consectetur adipiscing elit. Pellentesque tempus, magna vel fermentum consequat, orci odio lobortis eros, ut iaculis turpis ipsum ac dolor. Praesent mollis fermentum nunc ut condimentum. Maecenas vehicula eros metus, eu venenatis enim.</p></div>
    <div class="footer">ABOUT VESTA | CHP | STRANDED GAS | RESOURCES | PARTNERS AND SUPPLIERS | CONTACT US<br>2010 Vesta Power All Rights Reserved.</div>
  </div>
</section>

<section class="page page--inner">
  <div class="card">
    <div class="topband">
      <div class="utility">
        <svg viewBox="0 0 14 12"><path d="M1 6 7 1l6 5M3 5v6h8V5" fill="none" stroke="#b3d700" stroke-width="1.5"/></svg>
        <svg viewBox="0 0 14 12"><rect x="1" y="2" width="12" height="8" fill="none" stroke="#b3d700" stroke-width="1.5"/><path d="M1 2l6 5 6-5" fill="none" stroke="#b3d700" stroke-width="1.5"/></svg>
        <svg viewBox="0 0 14 12"><path d="M7 1v4M2 5h10M2 5v3M7 5v3M12 5v3" fill="none" stroke="#b3d700" stroke-width="1.5"/></svg>
      </div>
      <div class="brand">Vesta Power</div>
      <ul class="nav">
        <li>About Vesta</li><li>CHP</li><li class="current">Stranded Gas</li><li>Resources</li><li>Partners And Suppliers</li><li>Contact Us</li>
      </ul>
      <div class="main">
        <div class="article">
          <h1>Stranded Gas</h1>
          <p>Lorem ipsum dolor sit amet, consectetur adipiscing elit. Pellentesque tempus, magna vel fermentum consequat, orci odio lobortis eros, ut iaculis turpis ipsum ac dolor. Praesent mollis fermentum nunc ut condimentum. Maecenas vehicula eros metus, eu venenatis enim. Pellentesque eget est et justo semper dapibus. Suspendisse ut pharetra lectus. Suspendisse ut volutpat lectus. Cras turpis magna, iaculis id suscipit ut, aliquam at quam. Nam mattis mi ac odio pretium porta. In blandit lorem a lectus molestie scelerisque auctor massa consequat.</p>
          <p>Lorem ipsum dolor sit amet, consectetur adipiscing elit. Pellentesque tempus, magna vel fermentum consequat, orci odio lobortis eros, ut iaculis turpis ipsum ac dolor. Praesent mollis fermentum nunc ut condimentum. Maecenas vehicula eros metus, eu venenatis enim. Pellentesque eget est et justo semper dapibus. Suspendisse ut pharetra lectus. Suspendisse ut volutpat lectus. Cras turpis magna, iaculis id suscipit ut, aliquam at quam. Nam mattis mi ac odio pretium porta. In blandit lorem a lectus molestie scelerisque auctor massa consequat.</p>
          <p>Lorem ipsum dolor sit amet, consectetur adipiscing elit. Pellentesque tempus, magna vel fermentum consequat, orci odio lobortis eros, ut iaculis turpis ipsum ac dolor. Praesent mollis fermentum nunc ut condimentum. Maecenas vehicula eros metus, eu venenatis enim. Pellentesque eget est et justo semper dapibus. Suspendisse ut pharetra lectus. Suspendisse ut volutpat lectus. Cras turpis magna, iaculis id suscipit ut, aliquam at quam. Nam mattis mi ac odio pretium porta. In blandit lorem a lectus molestie scelerisque auctor massa consequat.</p>
          <p>Lorem ipsum dolor sit amet, consectetur adipiscing elit. Pellentesque tempus, magna vel fermentum consequat, orci odio lobortis eros, ut iaculis turpis ipsum ac dolor. Praesent mollis fermentum nunc ut condimentum. Maecenas vehicula eros metus, eu venenatis enim. Pellentesque eget est et justo semper dapibus. Suspendisse ut pharetra lectus. Suspendisse ut volutpat lectus.</p>
        </div>
        <div class="scroll"></div>
      </div>
    </div>
    <div class="tile tile--services"><span class="tile__label">Our Services</span><p>Lorem ipsum dolor sit amet, consectetur adipiscing elit. Pellentesque tempus, magna vel fermentum consequat, orci odio lobortis eros, ut iaculis turpis ipsum ac dolor. Praesent mollis fermentum nunc ut condimentum. Maecenas vehicula eros metus, eu venenatis enim.</p></div>
    <div class="feature">
      <div class="feature__photo" role="img" aria-label="Photo: water droplet on a green leaf"></div>
      <div class="feature__text"><p>Vesta Power provides its customers with clean, redundant and reliable power. Functioning as a private power producer, Vesta Power owns and operates combined heat and power (CHP) and distributed generation (DG) systems.</p><p>By using aero derivative turbine engines the company has the flexibility to use the best source of fuel for each site and power requirement. The turbine engine can operate on virtually any combustible fuel. This allows Vesta to utilize the flex fuel practice and operate on either the least expensive fuel available or operate on renewable and biofuels to fulfill the green power requirements mandated by many federal, state and local utility commissions.</p></div>
    </div>
    <div class="tile tile--contact"><span class="tile__label">Contac Us</span><p>Lorem ipsum dolor sit amet, consectetur adipiscing elit. Pellentesque tempus, magna vel fermentum consequat, orci odio lobortis eros, ut iaculis turpis ipsum ac dolor. Praesent mollis fermentum nunc ut condimentum. Maecenas vehicula eros metus, eu venenatis enim.</p></div>
    <div class="footer">ABOUT VESTA | CHP | STRANDED GAS | RESOURCES | PARTNERS AND SUPPLIERS | CONTACT US<br>2010 Vesta Power All Rights Reserved.</div>
  </div>
</section>

<section class="page page--slide">
  <div class="slide__frame" role="img" aria-label="Slide background: cloudy sky over green hills">
    <div class="slide__rule"></div>
    <div class="slide__panel"></div>
    <div class="slide__brand">Vesta Power</div>
  </div>
</section>

</body>
</html>
```